Payday Lending App Interface Design

Hello, we are building a payday lending application, Lendora, that lend people money. I have drafted some of the screens that show the functionalities we have at the moment, please find the screens in attachments.
The elements in the screens are placed just to show what should be included in those screens, it's not necessary to follow the same layout. If you have better design ideas, you are very welcomed to show off your talent.
I think what we want is a style guide so that we can apply the same style to any screens that are similar to the ones I attached. We really like
the style as in the attached image called Style.png. We might want something similar - a simple, clean design yet fun and engaging. Customised graphical elements such as icons, illustrations are preferable.
Apart from the attached screens, we might also need a design for the On Board screen and the Login/Sign Up screen too.
Our logo colour is in yellow and black. Perhaps we will have a similar colour theme. I also attached the logo file, icon-Lendora.png, if you would like to put it in your design.
Please message me if you need further information.
Regards
Target Market(s)
Young people that doesn't have strong income
Look and feel

```html
<!DOCTYPE html>
<html lang="en">
<head>
<meta charset="utf-8">
<title>Lendora – App Screens</title>
<link href="https://fonts.googleapis.com/css2?family=Roboto:wght@300;400;500;700&display=swap" rel="stylesheet">
<style>
  :root{
    --ink:#0a0a0c;
    --stage:#050508;
    --yellow:#fbd80d;
    --yellow-deep:#ecc600;
    --white:#ffffff;
    --paper:#f3f3f4;
    --grey-text:#9b9b9b;
    --muted:#c8c8c8;
    --line:#d6d6d6;
    --body:#5a4a00;
  }
  *{box-sizing:border-box;margin:0;padding:0}
  html,body{width:1200px;height:848px;overflow:hidden;background:var(--stage);font-family:'Roboto',sans-serif;color:var(--ink)}
  .canvas{position:relative;width:1200px;height:848px}
  .screen{position:absolute;top:89px;width:300px;height:662px;overflow:hidden}
  .abs{position:absolute}

  /* brand */
  .brand{display:flex;align-items:center;gap:6px;font-weight:700}
  .brand-square{width:14px;height:14px;border-radius:3px}

  /* home screen */
  .home{left:88px;background:linear-gradient(160deg,#ffffff 0%,#f1f1f2 45%,#e6e6e8 100%);border-radius:22px}
  .menu-icon{left:22px;top:45px;width:20px}
  .menu-icon span{display:block;height:3px;background:var(--ink);border-radius:2px;margin-bottom:3px}
  .menu-icon span:last-child{width:12px}
  .home-brand{left:50%;top:43px;transform:translateX(-50%);font-size:22px}
  .home-brand .brand-square{background:var(--yellow);width:18px;height:18px}
  .settings{left:258px;top:37px;width:20px;height:20px;background:#e4e4e6;border-radius:4px;display:flex;align-items:center;justify-content:center}
  .greeting{left:22px;top:128px;font-size:18px;font-weight:400}
  .timeline{left:27px;top:194px;width:5px;height:470px;background:var(--yellow)}
  .step-dot{left:22px;width:15px;height:15px;border-radius:50%;border:3px solid var(--ink);background:var(--yellow)}
  .step-title{left:62px;font-size:18px;font-weight:400;line-height:1.3}
  .step-card{left:46px;top:221px;width:220px;height:182px;background:var(--yellow);box-shadow:0 6px 14px rgba(0,0,0,.12)}
  .step-card h3{position:absolute;left:16px;top:12px;font-size:19px;font-weight:400;line-height:24px}
  .step-card p{position:absolute;left:16px;top:70px;width:196px;font-size:11.5px;line-height:16px;color:var(--body);font-weight:300}
  .btn-ghost{position:absolute;left:16px;top:138px;width:117px;height:30px;background:var(--white);font-size:11px;font-weight:500;display:flex;align-items:center;justify-content:center}
  .muted-copy{left:62px;top:506px;width:200px;font-size:11.5px;line-height:16px;color:var(--muted);font-weight:300}
  .btn-muted{left:62px;top:581px;width:93px;height:30px;background:rgba(255,255,255,.7);font-size:11px;font-weight:500;color:var(--muted);display:flex;align-items:center;justify-content:center}

  /* loan details */
  .loan{left:450px;background:linear-gradient(150deg,var(--yellow) 0%,var(--yellow) 55%,var(--yellow-deep) 100%)}
  .loan-brand{left:27px;top:58px;font-size:18px}
  .loan-brand .brand-square{background:var(--ink)}
  .screen-title{font-size:18px;font-weight:700;letter-spacing:.2px}
  .loan-title{right:28px;top:57px}
  .loan-card{left:27px;top:121px;width:248px;height:511px;background:var(--white);box-shadow:0 4px 12px rgba(0,0,0,.12)}
  .repay-summary{position:absolute;left:0;top:0;width:248px;height:231px;background:linear-gradient(160deg,#f7f7f8,#e9e9ea)}
  .repay-summary h2{position:absolute;top:21px;width:100%;text-align:center;font-size:18px;font-weight:500}
  .amount-badge{position:absolute;left:87px;top:45px;width:74px;height:74px;border-radius:50%;background:var(--yellow);display:flex;align-items:center;justify-content:center;font-size:24px;font-weight:500}
  .due-date{position:absolute;top:127px;width:100%;text-align:center;font-size:18px;font-weight:500}
  .progress{position:absolute;left:29px;top:162px;width:189px;height:31px;background:var(--white);box-shadow:0 1px 4px rgba(0,0,0,.12);display:flex;padding:3px;font-size:13px;font-weight:500}
  .progress span{flex:1;display:flex;align-items:center;justify-content:center}
  .progress .paid{background:var(--yellow)}
  .progress-labels{position:absolute;left:30px;top:199px;width:190px;display:flex;justify-content:space-between;font-size:11px}
  .activities{position:absolute;left:0;top:231px;width:248px}
  .activities h2{text-align:center;font-size:18px;font-weight:500;margin-top:34px}
  .activity{margin:16px 29px 0 29px;padding-bottom:14px;border-bottom:1px solid var(--line);display:flex;justify-content:space-between}
  .activity b{display:block;font-size:13.5px;font-weight:500}
  .activity small{display:block;font-size:11.5px;color:#666;margin-top:6px}
  .activity .sum{font-size:13.5px;font-weight:500}

  /* personal details */
  .personal{left:815px;background:var(--white)}
  .personal-head{position:absolute;left:0;top:0;width:300px;height:158px;background:linear-gradient(150deg,var(--yellow) 0%,var(--yellow) 60%,var(--yellow-deep) 100%)}
  .personal-brand{left:27px;top:38px;font-size:18px}
  .personal-brand .brand-square{background:var(--ink)}
  .personal-title{left:27px;top:84px}
  .personal-sub{left:27px;top:113px;font-size:11px;color:#6b5a00}
  .field{position:absolute;left:25px;width:251px;height:41px;background:var(--white);border:1px solid #ececec;box-shadow:0 2px 6px rgba(0,0,0,.08)}
  .field-chip{position:absolute;left:14px;top:-14px;width:73px;height:23px;background:var(--yellow);border-radius:3px;font-size:11px;display:flex;align-items:center;justify-content:center}
  .field-placeholder{position:absolute;left:13px;top:13px;font-size:11.5px;color:#555}
  .btn-primary{position:absolute;left:25px;top:475px;width:251px;height:39px;background:var(--yellow);font-size:11.5px;font-weight:700;display:flex;align-items:center;justify-content:center}
  .footer-art{position:absolute;left:0;top:527px;width:300px;height:135px;background:linear-gradient(180deg,#ffffff 0%,#fdf6cf 100%)}
</style>
</head>
<body>
<main class="canvas">

  <section class="screen home">
    <div class="abs menu-icon"><span></span><span></span></div>
    <div class="abs brand home-brand"><span class="brand-square"></span>Lendora</div>
    <div class="abs settings">
      <svg width="12" height="12" viewBox="0 0 24 24"><path fill="#0a0a0c" d="M19.4 13a7.5 7.5 0 0 0 0-2l2.1-1.6-2-3.5-2.5 1a7.7 7.7 0 0 0-1.7-1L15 3h-4l-.4 2.9a7.7 7.7 0 0 0-1.7 1l-2.5-1-2 3.5L6.6 11a7.5 7.5 0 0 0 0 2l-2.1 1.6 2 3.5 2.5-1a7.7 7.7 0 0 0 1.7 1L11 21h4l.4-2.9a7.7 7.7 0 0 0 1.7-1l2.5 1 2-3.5zM13 15.5a3.5 3.5 0 1 1 0-7 3.5 3.5 0 0 1 0 7z" transform="translate(-1 0)"/></svg>
    </div>
    <p class="abs greeting">Hi,User name</p>

    <div class="abs timeline"></div>
    <div class="abs step-dot" style="top:187px"></div>
    <p class="abs step-title" style="top:185px">Start</p>

    <article class="abs step-card">
      <h3>Upload your personal information</h3>
      <p>Lorem ipsum dolor sit amet, consec tetur adipiscing elit, sed do eiusmod tempor incididunt ut labore et dolore magna aliqua.</p>
      <span class="btn-ghost">UPLOAD NOW</span>
    </article>
    <div class="abs step-dot" style="top:236px"></div>

    <div class="abs step-dot" style="top:428px"></div>
    <p class="abs step-title" style="top:425px">Connect Bank Account</p>

    <div class="abs step-dot" style="top:478px"></div>
    <p class="abs step-title" style="top:474px">Apply a Loan</p>
    <p class="abs muted-copy">Lorem ipsum dolor sit amet, consec tetur adipiscing elit, sed do eiusmod tempor incididunt ut labore et dolore magna aliqua.</p>
    <span class="abs btn-muted">LEARN MORE</span>
  </section>

  <section class="screen loan">
    <div class="abs brand loan-brand"><span class="brand-square"></span>Lendora</div>
    <h1 class="abs screen-title loan-title">LOAN DETAILS</h1>
    <div class="abs loan-card">
      <div class="repay-summary">
        <h2>Next Repayment</h2>
        <div class="amount-badge">$XX</div>
        <p class="due-date">On 4 Dec</p>
        <div class="progress"><span class="paid">XXX</span><span>XXX</span></div>
        <div class="progress-labels"><span>Paid</span><span>Left</span></div>
      </div>
      <div class="activities">
        <h2>Activities</h2>
        <div class="activity"><div><b>Repayment</b><small>dd mm yy</small></div><span class="sum">$XX</span></div>
        <div class="activity"><div><b>Repayment</b><small>dd mm yy</small></div><span class="sum">$XX</span></div>
      </div>
    </div>
  </section>

  <section class="screen personal">
    <div class="personal-head"></div>
    <div class="abs brand personal-brand"><span class="brand-square"></span>Lendora</div>
    <h1 class="abs screen-title personal-title">PERSONAL DETAILS</h1>
    <p class="abs personal-sub">Please provide details as shown on ID</p>

    <div class="field" style="top:201px"><span class="field-chip">Given name</span></div>
    <div class="field" style="top:273px"><span class="field-chip">Middle name</span></div>
    <div class="field" style="top:345px"><span class="field-chip">Surname</span></div>
    <div class="field" style="top:409px"><span class="field-placeholder">Date of Birth (Day/Month/Year)</span></div>
    <span class="btn-primary">NEXT</span>

    <div class="footer-art" role="img" aria-label="Decorative line graphic with yellow dots marking a progress path"></div>
  </section>

</main>
</body>
</html>
```